Webbanner-Design für Beratungs-, Ausbildungs- und Forschungsunternehmen
Sehr schnelle Erstellung und Anpassung des Designs. Sehr gute Arbeit!
Zielgruppe
Wir sind ein Beratungs-, Ausbildungs- und Forschungsunternehmen im Bereich der chemischen instrumentellen Analytik.
Unsere Zielgruppe sind andere Unternehmen in unserem Bereich, deren Mitarbeiter*Innen, sowie Hochschulen und Wissenschaftler.
Für eine wissenschaftliche Veranstaltung suchen wir ein Banner, das die Sichtbarkeit der Veranstaltung im Vorfeld erhöhen soll.
Aufgabenstellung
Das Webbanner soltle alle wichtigen Informationen zur Veranstaltung, sowie unser Firmenlogo enthalten (Titel, Datum, Ort, Hinweis auf mögliche Online-Teilnahme)
Ein schlichtes Design wäre wünschenswert, es darf aber gerne auffallen. Das Banner soll zur Bewerbung der Veranstaltung auf Websiten und in den sozialen Medien genutzt werden
Die Größe soll W:768 x H:90 px sein. (mit Hyperlink)

```html
<!DOCTYPE html>
<html lang="de">
<head>
<meta charset="utf-8">
<title>Seminar GC meets NTS – Banner</title>
<link rel="stylesheet" href="https://fonts.googleapis.com/css2?family=Arimo:wght@400;700&display=swap">
<style>
  :root {
    --teal: #5cd3d0;
    --white: #ffffff;
    --date-red: #a8331c;
    --ink: #2f3a3a;
    --muted: #4d5656;
    --button: #333333;
  }
  * { margin: 0; padding: 0; box-sizing: border-box; }
  html, body { width: 1200px; height: 141px; overflow: hidden; background: var(--white); }
  body { font-family: "Arimo", Arial, sans-serif; }

  .banner {
    position: relative;
    display: block;
    width: 1200px;
    height: 141px;
    background: var(--teal);
    color: var(--white);
    text-decoration: none;
  }

  .brand {
    position: absolute;
    left: 0; top: 0;
    width: 227px; height: 141px;
    background: var(--white);
    display: flex;
    flex-direction: column;
    align-items: center;
    justify-content: center;
    gap: 10px;
  }
  .brand__name {
    display: flex;
    align-items: center;
    gap: 8px;
    font-size: 23px;
    font-weight: 700;
    color: var(--ink);
  }
  .brand__mark {
    width: 13px; height: 13px;
    border-radius: 50%;
    background: var(--teal);
  }
  .brand__tagline {
    font-size: 10px;
    font-weight: 700;
    text-align: center;
    color: var(--muted);
  }

  .seminar {
    position: absolute;
    left: 227px; width: 223px; top: 0; height: 141px;
    display: flex; flex-direction: column; justify-content: center; align-items: center;
    font-size: 19px; line-height: 31px;
  }
  .seminar__title { font-weight: 700; }

  .divider {
    position: absolute;
    top: 19px; height: 103px; width: 2px;
    background: var(--white);
  }
  .divider--first { left: 450px; }
  .divider--second { left: 805px; }

  .topic {
    position: absolute;
    left: 452px; width: 340px; top: 0; height: 141px;
    display: flex; flex-direction: column; justify-content: center; align-items: center;
    font-size: 18px; font-weight: 700; line-height: 25px;
    padding-bottom: 20px;
  }

  .dates {
    position: absolute;
    left: 850px; top: 11px;
    font-size: 17px; line-height: 20px;
  }
  .dates span { display: block; }
  .dates__day { color: var(--date-red); font-weight: 700; font-size: 19px; line-height: 22px; }
  .dates__place { font-size: 14px; line-height: 21px; }
  .dates__online { font-weight: 700; font-size: 19px; line-height: 22px; }

  .cta {
    position: absolute;
    left: 994px; top: 31px; width: 189px; height: 78px;
    background: var(--button);
    color: var(--white);
    display: flex; align-items: center; justify-content: center;
    font-size: 26px;
  }
</style>
</head>
<body>
<a class="banner" href="#">
  <div class="brand">
    <div class="brand__name"><span class="brand__mark"></span>Kellmar Analytik</div>
    <div class="brand__tagline">Beratung · Ausbildung · Forschung</div>
  </div>

  <div class="seminar">
    <span>Seminar</span>
    <span class="seminar__title">'GC meets NTS'</span>
  </div>

  <span class="divider divider--first"></span>

  <div class="topic">
    <span>- Gas Chromatography</span>
    <span>meets</span>
    <span>Non-Target Screening -</span>
  </div>

  <span class="divider divider--second"></span>

  <div class="dates">
    <span class="dates__day">04.02.2021</span>
    <span>and</span>
    <span class="dates__day">05.02.2021</span>
    <span class="dates__place">in Augsburg, Germany</span>
    <span class="dates__online">and online</span>
  </div>

  <div class="cta">Mehr Info</div>
</a>
</body>
</html>
```